Nimbus Crest Plan- Brindlow Insurance providing specialist Cyber and Liability Insurance

for Managed Technology Service Providers and their customer, we will use a letterhead that white labels insurer documents, which can be used in our physical letters as well as to be used within Email signatures.

Target Market(s)

Managed Technology Services Providers

Industry/Entity Type

Cyber Insurance

Requirements
Must have
• website, email address, contact phone numbers

```html
<!DOCTYPE html>
<html lang="en">
<head>
<meta charset="utf-8">
<title>Nimbus Crest Plan – Stationery</title>
<link rel="stylesheet" href="https://fonts.googleapis.com/css2?family=Lato:wght@400&family=Open+Sans:wght@400;600&display=swap">
<style>
  :root {
    --backdrop: #9a9a9a;
    --paper: #ffffff;
    --ink: #3d3d3d;
    --ink-soft: #555555;
    --charcoal: #4d4d4d;
    --green: #3bb54a;
    --on-dark: #ffffff;
  }
  * { margin: 0; padding: 0; box-sizing: border-box; }
  html, body { width: 1200px; height: 866px; overflow: hidden; }
  body { background: var(--backdrop); position: relative; font-family: "Open Sans", sans-serif; color: var(--ink); }

  .letterhead { position: absolute; left: 115px; top: 92px; width: 482px; height: 681px; background: var(--paper); overflow: hidden; }
  .business-card { position: absolute; left: 651px; top: 330px; width: 412px; height: 206px; background: var(--paper); overflow: hidden; }

  .brand { position: absolute; display: flex; align-items: center; gap: 7px; font-family: "Open Sans", sans-serif; font-weight: 600; color: var(--ink); white-space: nowrap; letter-spacing: 0.3px; }
  .brand-mark { width: 11px; height: 11px; background: var(--green); }
  .letterhead .brand { left: 33px; top: 38px; font-size: 20px; }
  .business-card .brand { left: 25px; top: 62px; font-size: 17px; }

  .contact-list { position: absolute; list-style: none; font-family: "Open Sans", sans-serif; color: var(--ink); }
  .contact-list li { display: flex; align-items: center; gap: 4px; white-space: nowrap; }
  .contact-list svg { width: 7px; height: 7px; flex: none; fill: var(--green); }
  .letterhead .contact-list { left: 303px; top: 36px; font-size: 8.8px; line-height: 11.7px; }
  .business-card .contact-list { left: 233px; top: 50px; font-size: 9.3px; line-height: 12px; }

  .recipient { position: absolute; left: 33px; top: 184px; font-family: "Lato", sans-serif; color: var(--ink-soft); }
  .recipient-name { font-size: 9.5px; letter-spacing: 0.2px; line-height: 14px; }
  .recipient-line { font-size: 6.8px; line-height: 12px; }

  .letter-body { position: absolute; left: 33px; top: 247px; width: 418px; font-family: "Lato", sans-serif; font-size: 7.1px; line-height: 11.8px; color: var(--ink-soft); text-align: justify; }
  .letter-body p + p { margin-top: 10px; }

  .sign-off { position: absolute; left: 33px; top: 433px; font-family: "Lato", sans-serif; color: var(--ink-soft); }
  .sign-off-greeting { font-size: 7.5px; line-height: 12px; }
  .signature { width: 90px; height: 22px; margin: 3px 0 4px; background: linear-gradient(90deg, #e4e4e4, #f2f2f2); border-radius: 2px; }
  .sign-off-name { font-size: 9px; }

  .footer-wave { position: absolute; left: 0; display: block; }
  .letterhead .footer-wave { top: 565px; width: 482px; height: 116px; }
  .business-card .footer-wave { top: 108px; width: 412px; height: 50px; }

  .disclaimer { position: absolute; left: 0; width: 100%; text-align: center; font-family: "Open Sans", sans-serif; }
  .disclaimer .statement { font-size: 8.2px; line-height: 10.3px; }
  .disclaimer .registration { font-size: 7.2px; line-height: 11px; }
  .disclaimer .dot { display: inline-block; width: 2.5px; height: 2.5px; border-radius: 50%; background: var(--green); vertical-align: middle; margin: 0 7px; }
  .letterhead .disclaimer { top: 641px; color: var(--on-dark); }
  .business-card .disclaimer { top: 166px; color: var(--ink); }
</style>
</head>
<body>

<svg width="0" height="0" style="position:absolute">
  <defs>
    <symbol id="icon-phone" viewBox="0 0 16 16"><path d="M3.6 1.2l2.3 2.7c.3.4.3.9 0 1.3L4.8 6.5c.9 2 2.6 3.7 4.7 4.7l1.3-1.1c.4-.3.9-.3 1.3 0l2.7 2.3c.4.3.4.9.1 1.3l-1.3 1.4c-.5.5-1.2.7-1.9.5C6.8 14.2 1.8 9.2.4 4.3.2 3.6.4 2.9.9 2.4L2.3 1.1c.4-.3 1-.3 1.3.1z"/></symbol>
    <symbol id="icon-mail" viewBox="0 0 16 16"><path d="M1 3h14v1.2L8 8.6 1 4.2z"/><path d="M1 5.8l7 4.4 7-4.4V13H1z"/></symbol>
    <symbol id="icon-globe" viewBox="0 0 16 16"><path d="M8 1a7 7 0 100 14A7 7 0 008 1zm0 1.6c.9 0 1.9 1.8 2.2 4.6H5.8C6.1 4.4 7.1 2.6 8 2.6zM2.7 8.8h1.6c.1 1.6.4 3 .9 4A5.4 5.4 0 012.7 8.8zm0-1.6a5.4 5.4 0 012.5-4c-.5 1-.8 2.4-.9 4zM8 13.4c-.9 0-1.9-1.8-2.2-4.6h4.4c-.3 2.8-1.300 4.6-2.2 4.6zm2.8-.6c.5-1 .8-2.4.9-4h1.6a5.4 5.4 0 01-2.5 4zm.9-5.6c-.1-1.6-.4-3-.9-4a5.4 5.4 0 012.5 4z"/></symbol>
  </defs>
</svg>

<section class="letterhead" aria-label="Letterhead">
  <div class="brand"><span class="brand-mark"></span>Nimbus Crest Plan</div>

  <ul class="contact-list">
    <li><svg><use href="#icon-phone"/></svg>+61 03 5550 1427</li>
    <li><svg><use href="#icon-mail"/></svg>insure@nimbuscrestplan.com.au</li>
    <li><svg><use href="#icon-globe"/></svg>www.nimbuscrestplan.com.au</li>
  </ul>

  <div class="recipient">
    <div class="recipient-name">DARREN HOLLOWAY</div>
    <div class="recipient-line">President / CEO</div>
    <div class="recipient-line">City/State, Zip Code</div>
  </div>

  <div class="letter-body">
    <p>Lorem Ipsum is simply dummy text of the printing and typesetting industry. Lorem Ipsum has been the industry's standard dummy text ever since the 1500s, when an unknown printer took a galley of type and scrambled it to make a type specimen book. It has survived not only five centuries, but also the leap into electronic typesetting, remaining essentially unchanged. It was popularised in the 1960s with the release of Quillmark sheets containing Lorem Ipsum passages, and more recently with desktop publishing software like Folio PageForge including versions of Lorem Ipsum.</p>
    <p>It is a long established fact that a reader will be distracted by the readable content of a page when looking at its layout. The point of using Lorem Ipsum is that it has a more-or-less normal distribution of letters, as opposed to using 'Content here, content here', making it look like readable English. Many desktop publishing packages and web page editors now use Lorem Ipsum as their default model text, and a search accident, sometimes on purpose (injected humour and the like).</p>
    <p>There are many variations of passages of Lorem Ipsum available, but the majority have suffered alteration in some form, by injected humour, or randomised words which don't look even slightly believable. If you are going to use a passage of Lorem Ipsum, you need to be sure there isn't anything embarrassing hidden in the middle of text.</p>
  </div>

  <div class="sign-off">
    <div class="sign-off-greeting">Sincerely,</div>
    <div class="signature" role="img" aria-label="Handwritten signature of Lena Marsh"></div>
    <div class="sign-off-name">Lena Marsh</div>
  </div>

  <svg class="footer-wave" viewBox="0 0 482 116" preserveAspectRatio="none" aria-hidden="true">
    <path d="M0 24 C70 62 250 70 464 9 C250 68 80 76 0 42 Z" fill="var(--green)"/>
    <path d="M0 43 C90 80 280 72 482 6 L482 116 L0 116 Z" fill="var(--charcoal)" stroke="var(--paper)" stroke-width="1.6"/>
  </svg>

  <div class="disclaimer">
    <div class="statement">Brindlow Insurance Services Pty Ltd (ABN 41 208 553 176) is an Authorised<br>Representative of Tarrowby Insurance Broking Pty Ltd (ABN 63 402 118 590 AFSL No 512904)</div>
    <div class="registration">ABN no. 41 208 553 176<span class="dot"></span>Corporate Authorised Representative no. 1390455</div>
  </div>
</section>

<section class="business-card" aria-label="Business card">
  <div class="brand"><span class="brand-mark"></span>Nimbus Crest Plan</div>

  <ul class="contact-list">
    <li><svg><use href="#icon-phone"/></svg>+61 03 5550 1427</li>
    <li><svg><use href="#icon-mail"/></svg>insure@nimbuscrestplan.com.au</li>
    <li><svg><use href="#icon-globe"/></svg>www.nimbuscrestplan.com.au</li>
  </ul>

  <svg class="footer-wave" viewBox="0 0 412 50" preserveAspectRatio="none" aria-hidden="true">
    <path d="M0 7 C60 45 220 52 393 2 C220 42 80 48 0 20 Z" fill="var(--green)"/>
  </svg>

  <div class="disclaimer">
    <div class="statement">Brindlow Insurance Services Pty Ltd (ABN 41 208 553 176) is an Authorised<br>Representative of Tarrowby Insurance Broking Pty Ltd (ABN 63 402 118 590 AFSL No 512904)</div>
    <div class="registration">ABN no. 41 208 553 176<span class="dot"></span>Corporate Authorised Representative no. 1390455</div>
  </div>
</section>

</body>
</html>
```